Commercial brochure presenting independent commercial activity

I would like to create a commercial brochure for my new professional activity.

This is a personal and not business oriented brochure because I will become an independent project assistant to assist engineering offices with one-off missions.

I want a 4 page A4 brochure

• Page 1: Logo, personal photo
• Page 2 and 3: Personal presentation and presentation of my activities
• Page4: contact information

My target audience: engineering offices and design offices

The objective of the brochure: it is to make my profile interesting so that design offices will want to use my services when there is demand

Sector of activity: food, chemical, pharmaceutical industry
The text of the brochure must remain in French and contain what is in the attached file

On page 1, you must keep a space for a photo of my profile which I will insert later because I do not have it yet and insert my monogram (it can be reworked to be inserted in the brochure)
The image with the logo (R/M) is the color range I want

Target Market(s)

engineering offices and design offices

Industry/Entity Type

industrie alimentaire, chimique, pharmaceutique

Font styles to use
Sans Serif

Colors
0094D4
00A9DD
6FCCEA
C7EBF8
E9F6FB

Requirements
Must have
• The plate must comply with current codes. Each reader must think that I am dynamic and that my services are of quality and equivalent to the presentation

```html
<!DOCTYPE html>
<html lang="fr">
<head>
<meta charset="utf-8">
<title>Brochure – Assistant de projet indépendant</title>
<link href="https://fonts.googleapis.com/css2?family=Montserrat:wght@500;600;800&family=Lato:wght@400;700&display=swap" rel="stylesheet">
<style>
  :root{
    --bg:#dcdcdf;
    --paper:#eeeeef;
    --ink:#141414;
    --blue-deep:#0a5fb0;
    --blue:#1d7fcd;
    --blue-light:#3199dd;
    --photo-grey:#616161;
    --shot-grey:#9a9a9a;
    --white:#ffffff;
  }
  *{margin:0;padding:0;box-sizing:border-box}
  html,body{width:1200px;height:840px;overflow:hidden;background:var(--bg)}
  body{font-family:"Lato",sans-serif;color:var(--ink)}
  .spread{position:absolute;left:80px;top:52px;width:1040px;height:736px;box-shadow:0 14px 30px rgba(0,0,0,.18)}
  .spread-shapes{position:absolute;inset:0}
  .page{position:absolute;top:0;width:520px;height:736px}
  .page--back{left:0}
  .page--front{left:520px}

  .work-shot{position:absolute;left:40px;top:0;width:320px;height:250px}

  .thanks-title{position:absolute;left:56px;top:300px;font-family:"Montserrat",sans-serif;font-weight:800;font-size:26px;letter-spacing:.5px}
  .thanks-text{position:absolute;left:56px;top:342px;width:400px;font-size:13px;line-height:1.35}

  .brand{position:absolute;display:flex;align-items:center;gap:10px}
  .brand-mark{width:14px;height:14px;border-radius:50%;flex:none}
  .brand-name{font-family:"Montserrat",sans-serif;font-weight:500;white-space:nowrap}
  .brand-role{font-family:"Montserrat",sans-serif;font-weight:500;white-space:nowrap}

  .brand--back{left:56px;top:440px;color:var(--blue-deep)}
  .brand--back .brand-mark{background:var(--blue-deep)}
  .brand--back .brand-name{font-size:30px}
  .role--back{position:absolute;left:80px;top:480px;font-size:13px;color:var(--blue-deep)}

  .contact-title{position:absolute;left:56px;top:530px;font-family:"Montserrat",sans-serif;font-weight:800;font-size:24px;letter-spacing:1px}
  .contact-list{position:absolute;left:56px;top:574px;list-style:none;font-size:13px;line-height:1.35}
  .contact-list li{display:flex;gap:10px;align-items:flex-start;margin-bottom:5px}
  .contact-list svg{width:15px;height:15px;flex:none;margin-top:1px}

  .brand--front{left:150px;top:100px;color:var(--white)}
  .brand--front .brand-mark{background:var(--white)}
  .brand--front .brand-name{font-size:26px}
  .role--front{position:absolute;left:174px;top:136px;font-size:11px;color:var(--white)}

  .photo-slot{position:absolute;left:180px;top:200px;width:380px;height:380px;display:flex;align-items:center;justify-content:center}
  .photo-label{position:absolute;left:200px;top:370px;width:340px;text-align:center;font-family:"Montserrat",sans-serif;font-weight:800;font-size:26px;letter-spacing:3px;color:var(--white)}

  .owner-name{position:absolute;left:40px;top:600px;font-family:"Montserrat",sans-serif;font-weight:600;font-size:18px;letter-spacing:2px;text-transform:uppercase}
  .headline{position:absolute;left:40px;top:630px;font-family:"Montserrat",sans-serif;font-weight:800;font-size:25px;line-height:1.08;letter-spacing:1.5px;color:var(--blue);text-transform:uppercase}
</style>
</head>
<body>
<div class="spread">
  <svg class="spread-shapes" viewBox="0 0 1040 736" width="1040" height="736" aria-hidden="true">
    <defs>
      <linearGradient id="blueFront" x1="0" y1="0" x2="1" y2="1">
        <stop offset="0" stop-color="#1e7fcf"/>
        <stop offset="1" stop-color="#2f9be0"/>
      </linearGradient>
      <linearGradient id="blueBack" x1="0" y1="0" x2="1" y2="1">
        <stop offset="0" stop-color="#0a5fb0"/>
        <stop offset="1" stop-color="#1670c0"/>
      </linearGradient>
      <clipPath id="backPage"><rect x="0" y="0" width="520" height="736"/></clipPath>
      <clipPath id="frontPage"><rect x="520" y="0" width="520" height="736"/></clipPath>
    </defs>
    <rect x="0" y="0" width="1040" height="736" fill="#eeeeef"/>

    <!-- back page -->
    <g clip-path="url(#backPage)">
      <path d="M250 0 H520 V230 C460 236 380 250 330 288 L250 288 Z" fill="url(#blueBack)"/>
      <circle cx="200" cy="55" r="240" fill="#eeeeef"/>
    </g>

    <!-- front page -->
    <g clip-path="url(#frontPage)">
      <rect x="520" y="0" width="520" height="600" fill="url(#blueFront)"/>
      <path d="M520 230 C590 250 630 320 640 440 L640 736 L520 736 Z" fill="#eeeeef"/>
      <path d="M700 572 C840 600 960 600 1040 590 L1040 736 L520 736 L520 560 Z" fill="#eeeeef"/>
      <circle cx="890" cy="390" r="205" fill="#eeeeef"/>
      <circle cx="890" cy="390" r="190" fill="#616161"/>
    </g>
    <line x1="520" y1="0" x2="520" y2="736" stroke="rgba(0,0,0,.06)" stroke-width="1"/>
  </svg>

  <section class="page page--back">
    <svg class="work-shot" viewBox="0 0 320 250" role="img" aria-label="Photo en noir et blanc d’un technicien travaillant sur un modèle 3D à l’écran">
      <defs>
        <linearGradient id="shotTone" x1="0" y1="0" x2="1" y2="1">
          <stop offset="0" stop-color="#bdbdbd"/>
          <stop offset="1" stop-color="#7d7d7d"/>
        </linearGradient>
        <clipPath id="shotClip"><circle cx="160" cy="55" r="228"/></clipPath>
      </defs>
      <rect x="-200" y="0" width="720" height="300" fill="url(#shotTone)" clip-path="url(#shotClip)"/>
    </svg>

    <h2 class="thanks-title">MERCI</h2>
    <p class="thanks-text">N'hésitez pas à me contacter pour discuter de vos besoins et découvrir comment je peux vous aider à atteindre vos objectifs.</p>

    <div class="brand brand--back"><span class="brand-mark"></span><span class="brand-name">A/F R/M</span></div>
    <p class="brand-role role--back">Assistant de projet indépendant</p>

    <h2 class="contact-title">CONTACT</h2>
    <ul class="contact-list">
      <li>
        <svg viewBox="0 0 24 24" fill="none" stroke="#0a5fb0" stroke-width="2" stroke-linecap="round" stroke-linejoin="round"><path d="M5 3h4l2 5-3 2a11 11 0 0 0 6 6l2-3 5 2v4a2 2 0 0 1-2 2A17 17 0 0 1 3 5a2 2 0 0 1 2-2z"/></svg>
        <span>+41 79 000 12 34</span>
      </li>
      <li>
        <svg viewBox="0 0 24 24" fill="none" stroke="#0a5fb0" stroke-width="2" stroke-linejoin="round"><rect x="3" y="5" width="18" height="14" rx="1"/><path d="M3 6l9 7 9-7"/></svg>
        <span>contact@af-rm-projets.ch</span>
      </li>
      <li>
        <svg viewBox="0 0 24 24" fill="none" stroke="#0a5fb0" stroke-width="2" stroke-linejoin="round"><path d="M3 11l9-8 9 8"/><path d="M5 10v10h14V10"/><rect x="10" y="14" width="4" height="6"/></svg>
        <span>Ch. des Tilleuls 8<br>1870 Valdorne</span>
      </li>
    </ul>
  </section>

  <section class="page page--front">
    <div class="brand brand--front"><span class="brand-mark"></span><span class="brand-name">A/F R/M</span></div>
    <p class="brand-role role--front">Assistant de projet indépendant</p>

    <p class="photo-label">VOTRE PHOTO</p>

    <p class="owner-name">A/F R/M</p>
    <h1 class="headline">Un atout précieux<br>pour votre<br>bureau d’études</h1>
  </section>
</div>
</body>
</html>
```